Construction Company Business Card

Business Card Design using new Logo

Contact Information for Business Card

include all company info and website

Requirements
Must have
• Wesley Corman - President
ph. 254-617-0382
Cedar Knoll, TX
wesley@ironmarkframing.com
www.ironmarkframing.com

```html
<!DOCTYPE html>
<html lang="en">
<head>
<meta charset="utf-8">
<title>Ironmark Framing – Business Card</title>
<link href="https://fonts.googleapis.com/css2?family=Poppins:wght@400;500;600&display=swap" rel="stylesheet">
<style>
  :root {
    --backdrop: #1f1f21;
    --brand-red: #b81c1f;
    --brand-red-light: #d0393c;
    --paper: #f6f6f4;
    --logo-grey: #8c8c92;
    --edge-grey: #b7b7bc;
    --white: #ffffff;
  }
  * { margin: 0; padding: 0; box-sizing: border-box; }
  html, body {
    width: 1200px;
    height: 874px;
    overflow: hidden;
    background: var(--backdrop);
    font-family: "Poppins", sans-serif;
  }
  .stage {
    position: relative;
    width: 1200px;
    height: 874px;
  }
  .card {
    position: absolute;
    left: 250px;
    width: 700px;
    height: 400px;
    overflow: hidden;
  }
  .card--front { top: 17px; background: var(--brand-red); }
  .card--back { top: 457px; background: var(--paper); }

  .brand-name {
    position: absolute;
    text-transform: uppercase;
    font-weight: 500;
    letter-spacing: 0.08em;
    white-space: nowrap;
    text-align: center;
  }
  .card--front .brand-name {
    left: 0; right: 0;
    top: 178px;
    font-size: 38px;
    color: var(--brand-red-light);
  }
  .card--back .brand-name {
    left: 400px;
    width: 230px;
    top: 194px;
    font-size: 18px;
    letter-spacing: 0.06em;
    color: var(--logo-grey);
  }

  .contact-panel {
    position: absolute;
    left: 0;
    top: 100px;
    width: 385px;
    height: 215px;
    background: var(--brand-red);
    color: var(--white);
    padding: 26px 0 0 40px;
  }
  .contact-name {
    font-size: 24px;
    font-weight: 600;
    text-transform: uppercase;
    letter-spacing: 0.02em;
    line-height: 1.1;
  }
  .contact-role {
    font-size: 15px;
    margin-bottom: 14px;
  }
  .contact-line {
    font-size: 15px;
    line-height: 1.45;
  }
  .edge-strip {
    position: absolute;
    right: 40px;
    top: 150px;
    width: 12px;
    height: 190px;
    background: var(--edge-grey);
  }
</style>
</head>
<body>
  <main class="stage">
    <section class="card card--front" aria-label="Card front">
      <p class="brand-name">Ironmark Framing</p>
    </section>

    <section class="card card--back" aria-label="Card back">
      <div class="contact-panel">
        <h1 class="contact-name">Wesley Corman</h1>
        <p class="contact-role">President</p>
        <p class="contact-line">Cedar Knoll, TX</p>
        <p class="contact-line">P-254-617-0382</p>
        <p class="contact-line">wesley@ironmarkframing.com</p>
        <p class="contact-line">www.ironmarkframing.com</p>
      </div>
      <p class="brand-name">Ironmark Framing</p>
      <div class="edge-strip"></div>
    </section>
  </main>
</body>
</html>
```